Lumiara Wine Label - Red Wine

We are a wine producing company based on the Oporto Metropolitan area.

We are looking to develop a label for a new red wine called "Lumiara". Lumiara is Portuguese for the well-known Spanish word Señorita, meaning a young lady. We want to make a label that reflects this young feeling with bright colours and fun designs while maintaining some elegance.

The target audience will be young people looking for a good time. Its preferred moments of consumption will be in social gatherings or fun times. We want to communicate fun.

We've attached the bottle model to be used, as well as some inspirational elements and our logo.
Updates

Low design quality

Target Market(s)

Young Consumers

Industry/Entity Type

Wine

Requirements
Must have
• Vintage year 2021, Red Wine mention

```html
<!DOCTYPE html>
<html lang="en">
<head>
<meta charset="UTF-8">
<title>Lumiara Wine – Red Wine Label</title>
<link rel="stylesheet" href="https://fonts.googleapis.com/css2?family=Allura&family=Cormorant+Garamond:wght@300;500&family=Montserrat:wght@400;700&family=Playfair+Display:wght@700&display=swap">
<style>
  :root {
    --stage: #1b1b1d;
    --stage-glow: #3a3a3c;
    --rose: #c4636f;
    --rose-ink: #2a1418;
    --cream: #eef2d4;
    --ink: #2b2b2b;
    --band: #1e1e20;
    --band-text: #f1f1ee;
  }
  * { margin: 0; padding: 0; box-sizing: border-box; }
  html, body { width: 1200px; height: 900px; overflow: hidden; }
  body {
    background: radial-gradient(ellipse at 50% 20%, var(--stage-glow) 0%, var(--stage) 60%);
    display: flex; align-items: center; justify-content: center; gap: 60px;
  }
  .neck-capsule {
    width: 150px; height: 170px; background: var(--rose);
    border-radius: 10px 10px 4px 4px;
    display: flex; flex-direction: column; align-items: center; justify-content: center;
    color: var(--rose-ink); font-family: "Playfair Display", serif; font-weight: 700;
    text-align: center; line-height: 1;
  }
  .neck-capsule .capsule-title { font-size: 17px; letter-spacing: 1px; }
  .neck-capsule .capsule-year { font-family: "Montserrat", sans-serif; font-size: 11px; margin-top: 12px; }
  .label { width: 600px; display: flex; flex-direction: column; }
  .tag-band {
    align-self: flex-end; margin-right: 70px; width: 300px; height: 74px; background: var(--rose);
    display: flex; flex-direction: column; align-items: center; justify-content: center;
    font-family: "Montserrat", sans-serif; font-weight: 700; font-size: 17px;
    color: var(--rose-ink); letter-spacing: 1px; line-height: 1.1; text-align: center;
  }
  .main-panel {
    position: relative; height: 380px; background: var(--cream);
    display: flex; flex-direction: column; align-items: center;
  }
  .main-panel .rules { position: absolute; inset: 0; }
  .figure-art {
    margin-top: 40px; width: 70px; height: 130px; border-radius: 40px 40px 20px 20px;
    background: linear-gradient(180deg, #e2e6c6, #d6dab8);
  }
  .brand-name {
    margin-top: 40px; font-family: "Cormorant Garamond", serif; font-weight: 500;
    font-size: 40px; letter-spacing: 9px; color: var(--ink); text-transform: lowercase;
  }
  .wine-type {
    font-family: "Allura", cursive; font-size: 66px; color: var(--ink); line-height: 1; margin-top: 4px;
  }
  .info-band {
    height: 130px; background: var(--band); color: var(--band-text);
    display: flex; flex-direction: column; align-items: center; justify-content: center;
    text-align: center; gap: 6px;
  }
  .vintage { font-family: "Montserrat", sans-serif; font-size: 24px; letter-spacing: 2px; }
  .tagline { font-family: "Montserrat", sans-serif; font-size: 10px; letter-spacing: 0.5px; line-height: 1.3; text-transform: uppercase; }
  .web { font-family: "Cormorant Garamond", serif; font-weight: 500; font-size: 14px; letter-spacing: 1px; }
</style>
</head>
<body>
  <div class="neck-capsule">
    <span class="capsule-title">WINE<br>RED</span>
    <span class="capsule-year">2021</span>
  </div>

  <div class="label">
    <div class="tag-band">
      <span>PERFECT</span>
      <span>AND EXCLUSIVE</span>
    </div>
    <div class="main-panel">
      <svg class="rules" width="600" height="380" viewBox="0 0 600 380" aria-hidden="true">
        <path d="M0 22 Q300 -4 600 22" fill="none" stroke="#2b2b2b" stroke-width="1"/>
        <line x1="40" y1="232" x2="150" y2="232" stroke="#2b2b2b" stroke-width="1"/>
        <line x1="450" y1="232" x2="560" y2="232" stroke="#2b2b2b" stroke-width="1"/>
        <path d="M30 340 Q300 360 570 340" fill="none" stroke="#2b2b2b" stroke-width="1"/>
      </svg>
      <div class="figure-art" role="img" aria-label="Fine line drawing of a young lady in a wide-brimmed hat"></div>
      <div class="brand-name">lumiara</div>
      <div class="wine-type">Wine</div>
    </div>
    <div class="info-band">
      <div class="vintage">2021</div>
      <div class="tagline">Red wine from the Oporto region<br>made for bright moments together</div>
      <div class="web">~<br>lumiara-wines.pt</div>
    </div>
  </div>
</body>
</html>
```